Property Management company

We need a design for our company Maplecrest Elder Residences. We are complex of apartments that we manage and operate. We do like the colors green or blue

Industry/Entity Type

Property Management,

Requirements
Must have
• color
Nice to have
• maybe be able to use as a watermark

```html
<!DOCTYPE html>
<html lang="en">
<head>
<meta charset="utf-8">
<title>Maplecrest Elder Residences – Letterhead</title>
<link rel="stylesheet" href="https://fonts.googleapis.com/css2?family=Montserrat:wght@700&family=Open+Sans:wght@300;400&family=Arimo:wght@400&family=Pinyon+Script&display=swap">
<style>
  :root {
    --backdrop: #e4e4e4;
    --paper: #f1f1f1;
    --ink: #1c1c24;
    --body-ink: #3a3a3a;
    --brand-blue: #2f3ae0;
    --brand-violet: #3a28e0;
    --brand-sky: #1b94e8;
    --brand-night: #0e1a2c;
    --white: #ffffff;
  }
  * { box-sizing: border-box; margin: 0; padding: 0; }
  html, body {
    width: 1200px; height: 1200px; overflow: hidden;
    background: var(--backdrop);
  }
  .letterhead {
    position: absolute;
    left: 196px; top: 30px;
    width: 807px; height: 1140px;
    background: var(--paper);
  }
  .brand {
    position: absolute;
    left: 64px; top: 52px;
    display: flex; align-items: center; gap: 10px;
  }
  .brand-mark {
    width: 14px; height: 14px;
    background: var(--brand-blue);
  }
  .brand-name {
    font-family: "Montserrat", sans-serif;
    font-weight: 700;
    font-size: 15px;
    line-height: 1.35;
    letter-spacing: 2px;
    text-transform: uppercase;
    color: var(--ink);
  }
  .contact {
    position: absolute;
    left: 523px; top: 80px;
    padding-left: 18px;
    border-left: 3px solid var(--brand-blue);
    font-family: "Arimo", sans-serif;
    font-size: 13px;
    line-height: 16px;
    color: var(--ink);
  }
  .contact-line { display: flex; align-items: center; gap: 8px; }
  .contact-line svg { width: 10px; height: 10px; flex: none; }
  .letter {
    position: absolute;
    left: 109px; width: 589px;
    font-family: "Open Sans", sans-serif;
    font-weight: 300;
    font-size: 13.4px;
    line-height: 19px;
    color: var(--body-ink);
  }
  .salutation { top: 269px; }
  .letter-body { top: 307px; text-align: justify; }
  .letter-body p + p { margin-top: 19px; }
  .closing { top: 780px; }
  .signature {
    position: absolute;
    left: 114px; top: 810px;
    font-family: "Pinyon Script", cursive;
    font-size: 26px;
    color: var(--ink);
  }
  .footer-band {
    position: absolute;
    left: 0; bottom: 18px;
    width: 100%; height: 36px;
    background: linear-gradient(90deg, var(--brand-violet) 0%, var(--brand-blue) 30%, var(--brand-sky) 84%, var(--brand-night) 84%, var(--brand-night) 100%);
    display: flex; align-items: center;
  }
  .footer-address {
    padding-left: 69px;
    font-family: "Arimo", sans-serif;
    font-size: 13.4px;
    color: var(--white);
  }
  .footer-mark {
    position: absolute;
    left: 685px; top: 0;
    width: 36px; height: 36px;
    border-radius: 50%;
    background: var(--white);
    border: 2px solid var(--brand-blue);
  }
</style>
</head>
<body>
  <main class="letterhead">
    <header>
      <div class="brand">
        <span class="brand-mark"></span>
        <div class="brand-name">Maplecrest<br>Elder Residences</div>
      </div>
      <address class="contact" style="font-style:normal">
        <div class="contact-line">
          <svg viewBox="0 0 10 10"><path d="M2 1 L4 1 L4.6 3 L3.4 3.8 Q4.4 5.8 6.2 6.6 L7 5.4 L9 6 L9 8 Q9 9 8 9 Q1 8.6 1 2 Q1 1 2 1Z" fill="var(--brand-blue)"/></svg>
          <span>(555) 318-2740</span>
        </div>
        <div class="contact-line">
          <svg viewBox="0 0 10 10"><rect x="0.5" y="2" width="9" height="6" fill="var(--brand-blue)"/><path d="M0.5 2 L5 5.5 L9.5 2" stroke="var(--paper)" stroke-width="1" fill="none"/></svg>
          <span>info@maplecrestelder.com</span>
        </div>
        <div class="contact-line">
          <svg viewBox="0 0 10 10"><circle cx="5" cy="5" r="4.2" fill="none" stroke="var(--brand-blue)" stroke-width="1"/><ellipse cx="5" cy="5" rx="1.8" ry="4.2" fill="none" stroke="var(--brand-blue)" stroke-width="0.8"/><path d="M0.8 5 H9.2" stroke="var(--brand-blue)" stroke-width="0.8"/></svg>
          <span>www.maplecrestelder.com</span>
        </div>
      </address>
    </header>

    <p class="letter salutation">Dear Daniel Whitcombe,</p>

    <section class="letter letter-body">
      <p>Lorem ipsum dolor sit amet, consectetuer adipiscing elit, sed diam nonummy nibh euismod tincidunt ut laoreet dolore magna aliquam erat volutpat. Ut wisi enim ad minim veniam, quis nostrud exerci tation ullamcorper suscipit lobortis nisl ut aliquip ex ea commodo consequat. Duis dolore te feugait nulla facilisi. Nam liber tempor cum soluta nobis eleifend option congue nihil imperdiet doming id quod mazim placerat facer possim assum. Lorem ipsum dolor sit amet, consectetuer adipiscing elit, sed diam nonummy nibh euismod tincidunt ut laoreet dolore magna aliquam erat volutpat. Ut wisi enim ad minim veniam, quis nostrud exerci tation ullamcorper suscipit lobortis nisl ut aliquip ex ea commodo consequat.</p>
      <p>Consectetuer adipiscing elit, sed diam nonummy nibh euismod tincidunt ut laoreet dolore magna aliquam erat volutpat. Ut wisi enim ad minim veniam, quis nostrud exerci tation ullamcorper suscipit lobortis nisl ut aliquip ex ea commodo consequat. Consectetuer adipiscing elit, sed diam nonummy nibh euismod tincidunt ut laoreet dolore magna aliquam erat volutpat. Ut wisi enim ad minim veniam, quis nostrud exerci tation ullamcorper suscipit lobortis nisl ut aliquip ex ea commodo consequat.</p>
      <p>Consectetuer adipiscing elit, sed diam nonummy nibh euismod tincidunt ut laoreet dolore magna aliquam erat volutpat. Ut wisi enim ad minim veniam, quis nostrud exerci tation ullamcorper suscipit lobortis nisl ut aliquip ex ea commodo consequat. Consectetuer adipiscing elit, sed diam nonummy nibh euismod tincidunt ut laoreet dolore magna aliquam erat volutpat. Ut wisi enim ad minim veniam, quis nostrud exerci tation ullamcorper suscipit lobortis nisl ut aliquip ex ea commodo consequat.</p>
    </section>

    <p class="letter closing">Sincerely Yours</p>
    <p class="signature">Marcus Hollander</p>

    <footer class="footer-band">
      <span class="footer-address">2480 Harlow Ridge Rd, Alder Falls, OH 43921</span>
      <span class="footer-mark"></span>
    </footer>
  </main>
</body>
</html>
```